Bright, Fun and hard to forget home inspection business card.

We need a Business card design for a new Home Inspection company. We are building a brand that is bright, fun and easy to remember.

Target Market(s)

Anyone involed in buying and selling of homes.

Industry/Entity Type

Home Inspection

Contact Information for Business Card

Colin Hartwell Owner/Inspector

Wedsite- KestrelHouseCheck.example
Phone: 253-555-0147
Email- ColinHartwell@mailbox.example
WA Lic # 4738

Requirements
Must have
• BQRV LOGO somewhere on card.

```html
<!DOCTYPE html>
<html lang="en">
<head>
<meta charset="utf-8">
<title>Kestrel House Check – Business Card</title>
<link rel="stylesheet" href="https://fonts.googleapis.com/css2?family=Oswald:wght@400;500&family=Pathway+Gothic+One&display=swap">
<style>
  :root {
    --bg: #3b3d40;
    --orange: #f15a29;
    --orange-deep: #d9481c;
    --white: #ffffff;
    --ink: #231f20;
    --edge: #c9c9c9;
    --shadow: rgba(0,0,0,0.45);
  }
  * { box-sizing: border-box; margin: 0; padding: 0; }
  html, body { width: 1200px; height: 1000px; overflow: hidden; }
  body { background: var(--bg); position: relative; font-family: "Pathway Gothic One", sans-serif; }

  .card-stack { position: absolute; width: 300px; height: 517px; }
  .stack-left { left: 179px; top: 235px; }
  .stack-right { left: 712px; top: 236px; }

  .card-layer {
    position: absolute; width: 286px; height: 503px;
    background: var(--orange-deep);
    box-shadow: 2px 3px 6px var(--shadow);
  }
  .layer-3 { left: 14px; top: 14px; }
  .layer-2 { left: 7px; top: 7px; }
  .stack-left .layer-2 { background: linear-gradient(var(--orange-deep) 0 27%, var(--edge) 27% 96%, var(--orange-deep) 96%); }

  .card { position: absolute; left: 0; top: 0; width: 286px; height: 503px; overflow: hidden; box-shadow: 1px 2px 5px var(--shadow); }

  /* Front */
  .card-front { background: var(--white); }
  .front-header {
    height: 137px; background: var(--orange);
    display: flex; align-items: center; justify-content: center; gap: 10px;
  }
  .brand-dot { width: 34px; height: 34px; border-radius: 50%; background: var(--white); flex: none; }
  .brand-name {
    font-family: "Oswald", sans-serif; font-weight: 400; color: var(--white);
    font-size: 27px; line-height: 1.0; text-transform: uppercase; letter-spacing: 0.5px;
  }
  .holder-name {
    font-family: "Oswald", sans-serif; font-weight: 500; color: var(--ink);
    font-size: 33px; text-align: center; letter-spacing: 0.5px;
    margin-top: 26px; transform: scaleX(0.82);
  }
  .holder-role {
    display: flex; align-items: center; gap: 10px; margin-top: 25px;
    font-size: 15px; color: #444; letter-spacing: 0.5px;
  }
  .holder-role::before, .holder-role::after { content: ""; flex: 1; height: 2px; background: var(--orange); }
  .contact-list { list-style: none; margin-top: 36px; padding-left: 28px; padding-right: 8px; }
  .contact-row { display: flex; align-items: center; height: 44px; }
  .contact-label {
    flex: none;
    width: 50px; height: 18px; border-radius: 9px; background: var(--orange);
    color: var(--white); font-size: 13px; text-align: center; line-height: 18px;
    margin-right: 26px;
  }
  .contact-value {
    flex: none; white-space: nowrap;
    font-size: 15.5px; color: var(--ink); letter-spacing: 0.3px;
  }
  .front-footer { position: absolute; left: 0; bottom: 0; width: 100%; height: 20px; background: var(--orange); }

  /* Back */
  .card-back { background: var(--orange); }
  .back-brand {
    position: absolute; left: 22px; top: 300px;
    display: flex; align-items: center; gap: 10px;
  }
  .back-brand .brand-name { font-size: 30px; }
</style>
</head>
<body>

  <section class="card-stack stack-left" aria-label="Business card front">
    <div class="card-layer layer-3"></div>
    <div class="card-layer layer-2"></div>
    <article class="card card-front">
      <header class="front-header">
        <span class="brand-dot"></span>
        <span class="brand-name">Kestrel<br>House Check<br>LLC</span>
      </header>
      <h1 class="holder-name">COLIN HARTWELL</h1>
      <p class="holder-role">Owner | Inspector</p>
      <ul class="contact-list">
        <li class="contact-row"><span class="contact-label">phone</span><span class="contact-value">253.555.0147</span></li>
        <li class="contact-row"><span class="contact-label">email</span><span class="contact-value">ColinHartwell@mailbox.example</span></li>
        <li class="contact-row"><span class="contact-label">web</span><span class="contact-value">KestrelHouseCheck.example</span></li>
        <li class="contact-row"><span class="contact-label">wa lic</span><span class="contact-value"># 4738</span></li>
      </ul>
      <div class="front-footer"></div>
    </article>
  </section>

  <section class="card-stack stack-right" aria-label="Business card back">
    <div class="card-layer layer-3"></div>
    <div class="card-layer layer-2"></div>
    <article class="card card-back">
      <div class="back-brand">
        <span class="brand-dot"></span>
        <span class="brand-name">Kestrel<br>House Check</span>
      </div>
    </article>
  </section>

</body>
</html>
```